Tech Laundry service company looking for a new modern and clean web site

Our site is www.brisklinenhub.com we are looking to rebrand our whole website.

We offer free pickup and delivery for laundry and dry cleaning in the NYC area. we target residential customers.

Sites to compare are www.trypolvex.com and www.zentumo.com
Most content can be found at www.brisklinenhub.com

We are looking for a clean and modern look. Nothing to busy

colors and font we use are
Logo font: Harabara
Slogan font: Swiss 721 Light Extended BT

Dark blue: C 100 M 88 Y 0 K 0
Light blue: C 85 M 50 Y 0 K 0
Orange: C 0 M 80 Y 95 K 0

Violet: C 85 M 100 Y 0 K 0

We use only Marlo, Quilse and vendrax
We are provide eco-friendly
next day laundry service

Our mission Statement is to deliver the Cleanest and Brightest clothes in the market. we use only top of the line

"We are the #1 proud supporter of Marlo and Quilse"

There will be 4 pages
the home page
and a 2 page scheduling page

THE HOME PAGE-
navigation bar must include

Home,
Clean my Clothes (schedule a pickup)
Pricing
Blog
Service Area
Commercial/Wholesale
Sign in
must have key elements about our business such as:
1. Our Price is 1.10 a lb
2. "New customers get 50% off first order and 100% off second order!"
3. we have next day service on all laundry orders
Again, you can pull the content off our current website brisklinenhub.com

Order Page-

Attached please find 5 steps of the ordering page. We are looking to condense into 2
we want step2+step3+step4 on one page
then step1+step5 on the second page on step5 we want the coinbird logo attached as well (as we do all credit card processing through CoinBird)
at the end of the process we want to offer them to create a password to auto register
the order confirmation is attached as well. we need all that info but would like it to seem cleaner and modern.

PRICING PAGE-

Wash and Fold 1.10 per Lb ($27 min charge)
Blankets $12 and up
Bathroom Rugs $5.00 and up

Dry Cleaning
Launder and Press shirt 1.25
Suit Jacket 6.00
Pants and Skirts 6.00
2 pc suit 12.00
Dress 10.00 and up
Blouses & Sweaters 6.00

Again, we are looking for a clean and sleek site not to busy.

Based on this we will be needed another 6-8 pages of design work that will be negotiated with the winner at the end of this contest.
Good Luck!

Target Market(s)

our customers are between the ages of 22-40 years old all live in NYC

Industry/Entity Type

Dry Cleaning

Number of Pages Required

4 page

Font styles to use
Other font styles liked:
• Harabara

Requirements
Must have
• sleek and cool design
• see www.polvex.com and zentumo.com for concept
• Our current site is brisklinenhub.com which we are looking to rebrand
Nice to have
• colors and font we use are
• Logo font: Harabara
• Slogan font: Swiss 721 Light Extended BT
• Dark blue: C 100 M 88 Y 0 K 0
• Light blue: C 85 M 50 Y 0 K 0
• Orange: C 0 M 80 Y 95 K 0
• Violet: C 85 M 100 Y 0 K 0
Should not have
• we want all the colors to be uniform. we are sending a message that we are the brightest and cleanest laundry service in the city!

```html
<!DOCTYPE html>
<html lang="en">
<head>
<meta charset="utf-8">
<title>Brisk Linen Hub — Laundry Pickup &amp; Delivery</title>
<link href="https://fonts.googleapis.com/css2?family=Roboto:wght@400;500;700&family=Tinos:ital,wght@0,400;1,400;1,700&display=swap" rel="stylesheet">
<style>
:root{
  --orange:#f05a28;
  --blue:#1f74c4;
  --blue-bright:#2b8ae0;
  --ink:#2e2e2e;
  --text:#444;
  --muted:#777;
  --light:#f3f2f0;
  --line:#d9e3ee;
  --dark:#2d2d2d;
  --darker:#272727;
  --white:#fff;
}
*{margin:0;padding:0;box-sizing:border-box}
html,body{width:1200px;height:3750px;overflow:hidden}
body{font-family:"Roboto",Arial,sans-serif;color:var(--text);background:var(--white);position:relative}
section,header,nav,footer{position:absolute;left:0;width:1200px}
.center{text-align:center}

/* hero */
.hero{top:0;height:770px}
.hero-bg{position:absolute;inset:0;background:radial-gradient(ellipse at 70% 30%,#6d6f72 0%,#3d3f42 45%,#1f2022 100%)}
.hero-brand{position:absolute;top:150px;left:0;width:100%;display:flex;justify-content:center;align-items:center;gap:14px}
.hero-brand .dot{width:84px;height:84px;border-radius:50%;background:var(--blue);border:5px solid var(--white)}
.hero-brand span{color:var(--white);font-weight:700;font-size:26px}
.mission{position:absolute;left:0;top:336px;width:100%;color:var(--white);font-weight:500;font-size:39px;line-height:52px;letter-spacing:1px;text-transform:uppercase}
.hero-lede{position:absolute;left:0;top:458px;width:100%;color:#e8e8e8;font-family:"Tinos",serif;font-style:italic;font-size:25px}
.hero-phone{position:absolute;left:0;top:505px;width:100%;color:var(--orange);font-size:39px;font-weight:500}
.btn-read{position:absolute;top:612px;left:442px;width:318px;height:76px;border-radius:38px;background:var(--blue);color:var(--white);font-size:27px;font-weight:500;display:flex;align-items:center;justify-content:center}

/* nav */
.topnav{top:770px;height:78px;background:#1e1e1e;display:flex;align-items:center}
.nav-logo{position:absolute;left:76px;display:flex;align-items:center;gap:10px;color:var(--white);font-weight:700;font-size:24px}
.nav-logo i{width:34px;height:34px;border-radius:50%;border:3px solid var(--white)}
.nav-links{position:absolute;left:322px;display:flex;align-items:center;list-style:none;font-size:13px;color:var(--white);font-weight:500;white-space:nowrap}
.nav-links li{padding:0 10px;border-right:1px solid #777;line-height:16px}
.nav-links li:last-child{border:none}
.btn-register{position:absolute;left:1022px;top:19px;width:102px;height:40px;border-radius:20px;background:var(--blue-bright);color:var(--white);font-size:15px;display:flex;align-items:center;justify-content:center}

/* quality */
.quality{top:848px;height:269px}
.section-title{color:var(--orange);font-size:36px;font-weight:500;text-transform:uppercase;letter-spacing:.5px}
.quality .section-title{margin-top:58px}
.quality p{margin-top:14px;font-size:24px;line-height:33px;color:var(--ink)}

/* five star */
.five-star{top:1117px;height:429px;background:var(--light)}
.five-star h2{position:absolute;left:100px;top:68px;color:var(--blue);font-size:36px;font-weight:500}
.five-star h3{position:absolute;left:100px;top:120px;font-size:15px;font-weight:700;color:#555}
.five-star p{position:absolute;left:100px;top:176px;width:560px;font-size:17px;line-height:30px;color:var(--muted)}
.btn-start{position:absolute;left:100px;top:305px;width:196px;height:46px;border-radius:23px;background:var(--orange);color:var(--white);font-size:17px;font-weight:500;display:flex;align-items:center;justify-content:center}
.five-star-photo{position:absolute;left:685px;top:0;width:440px;height:429px;background:linear-gradient(160deg,#e9e9ef 0%,#b9c3e0 45%,#c7a77a 100%)}

/* convenient */
.convenient{top:1546px;height:504px}
.convenient .section-title{margin-top:66px}
.steps{position:absolute;top:148px;left:0;width:100%}
.step{position:absolute;width:260px;text-align:center}
.step svg{display:block;margin:0 auto}
.step span{display:block;margin-top:14px;color:var(--blue);font-size:17px;font-style:italic;font-weight:500;text-transform:uppercase}
.perks{position:absolute;top:349px;left:78px;width:1083px;display:grid;grid-template-columns:repeat(3,1fr);gap:6px 8px}
.perk{height:48px;border:1px solid var(--line);display:flex;align-items:center;gap:10px;padding-left:14px;color:var(--orange);font-style:italic;font-size:17px}
.perk i{width:22px;height:22px;border-radius:50%;border:2px solid var(--blue-bright);flex:none}

/* testimonial */
.testimonial{top:2050px;height:433px}
.testimonial-bg{position:absolute;inset:0;background:radial-gradient(ellipse at 50% 40%,#4a4b4d 0%,#2a2b2d 60%,#18191a 100%)}
.testimonial h2{position:absolute;left:0;top:80px;width:100%;color:var(--blue-bright);font-size:36px;font-weight:500}
.testimonial blockquote{position:absolute;left:0;top:194px;width:100%;color:var(--white);font-family:"Tinos",serif;font-style:italic;font-weight:700;font-size:25px}
.testimonial cite{position:absolute;left:0;top:245px;width:100%;display:block;text-align:center;color:var(--blue-bright);font-family:"Tinos",serif;font-style:italic;font-weight:700;font-size:23px}
.dots{position:absolute;left:0;top:336px;width:100%;display:flex;justify-content:center;gap:10px}
.dots i{width:10px;height:10px;border-radius:50%;background:#bbb}
.dots i:nth-child(2){background:var(--white)}

/* service cards */
.services{top:2483px;height:387px}
.card{position:absolute;top:59px;width:448px;height:272px}
.card .photo{position:absolute;inset:0}
.card-a{left:132px}
.card-a .photo{background:linear-gradient(135deg,#aab7c4 0%,#e4e6e9 50%,#f7f7f7 100%)}
.card-b{left:608px}
.card-b .photo{background:linear-gradient(135deg,#c9ccd0 0%,#4a79c4 55%,#274a86 100%)}
.card-caption{position:absolute;left:20px;bottom:18px;color:var(--white)}
.card-caption strong{display:block;font-size:19px;font-weight:500}
.card-a strong{color:var(--blue)}
.card-b strong{color:var(--orange)}
.card-caption small{font-size:12px;color:#f2f2f2}
.card-a small{color:#555}

/* clients */
.clients{top:2870px;height:329px;background:var(--light)}
.clients .section-title{margin-top:52px}
.clients .subtitle{margin-top:10px;font-family:"Tinos",serif;font-style:italic;font-size:20px;color:#555}
.client-row{position:absolute;top:200px;left:190px;width:820px;display:flex;justify-content:space-between;align-items:center}
.client{display:flex;align-items:center;gap:10px;font-size:30px;font-weight:700;color:#3c3c3c}
.client i{width:30px;height:30px;border-radius:50%;background:#bbb}

/* call band */
.callband{top:3199px;height:150px;background:var(--dark);display:flex;align-items:center;justify-content:center}
.callband p{color:var(--blue-bright);font-size:35px;font-weight:500;text-transform:uppercase}
.callband span{color:var(--orange)}

/* footer */
.site-footer{top:3349px;height:401px;background:var(--darker);color:var(--white)}
.col{position:absolute;top:84px;width:300px;text-align:center}
.col h4{font-size:24px;font-weight:700;margin-bottom:16px}
.col ul{list-style:none;font-size:13px;line-height:28px}
.col-links{left:100px}
.col-contact{left:450px}
.col-address{left:802px}
.col-contact .email{color:var(--orange);font-size:14px}
.col-contact p,.col-address p{font-size:14px;line-height:28px}
.social{display:flex;justify-content:center;gap:12px;margin-top:16px;font-size:12px;color:#ccc}
.social li{display:flex;align-items:center;gap:4px}
.social i{width:10px;height:10px;border-radius:50%;background:#ccc}
.legal{position:absolute;left:0;top:346px;width:100%;text-align:center;font-family:"Tinos",serif;font-style:italic;font-size:13px;color:#ccc}
.contact-tab{position:absolute;left:887px;top:362px;width:238px;height:39px;background:var(--orange);border-radius:4px 4px 0 0;color:var(--white);font-size:14px;padding:10px 0 0 10px}
</style>
</head>
<body>

<header class="hero">
  <div class="hero-bg" role="img" aria-label="Row of commercial washing machines in a laundromat"></div>
  <div class="hero-brand"><i class="dot"></i><span>Brisk Linen Hub</span></div>
  <h1 class="mission center">Our mission statement is to deliver<br>the cleanest and brightest clothes in the market.</h1>
  <p class="hero-lede center">Lorem Ipsum is simply dummy text of the printing and typesetting industry. Lorem Ipsum has been the industry's.</p>
  <p class="hero-phone center">(212) 555-0148</p>
  <a class="btn-read">READ MORE</a>
</header>

<nav class="topnav">
  <div class="nav-logo"><i></i>Brisk Linen Hub</div>
  <ul class="nav-links">
    <li>Home</li><li>Clean my Clothes</li><li>Pricing</li><li>Blog</li><li>Service Area</li><li>Commercial/Wholesale</li><li>Sign in</li>
  </ul>
  <a class="btn-register">Register</a>
</nav>

<section class="quality center">
  <h2 class="section-title">Quality Assurance.</h2>
  <p>Every piece of laundry is handle with care by our trained attendants,<br>we guarantee our service by double checking you wont have<br>any missing clothes before delivery.</p>
</section>

<section class="five-star">
  <h2>5 STAR CUSTOMER SERVICE</h2>
  <h3>BEST RATED COMMERCIAL AND RESIDENTIAL LAUNDRY SERVICE</h3>
  <p>Our 5 Star Customer Service and quality assurance process sets up apart from other laundry service providers. Over 6 years Serving New York City and thousand of satisfied Customers.</p>
  <a class="btn-start">Get Started Now</a>
  <div class="five-star-photo" role="img" aria-label="Smiling attendant holding a basket of colourful laundry"></div>
</section>

<section class="convenient center">
  <h2 class="section-title">Convenient Laundry Service</h2>
  <div class="steps">
    <div class="step" style="left:95px">
      <svg width="116" height="116" viewBox="0 0 116 116"><circle cx="58" cy="58" r="55" fill="#fff" stroke="#ccc" stroke-width="3"/><rect x="32" y="36" width="44" height="40" rx="4" fill="#f05a28"/><rect x="36" y="48" width="36" height="24" fill="#fff"/><circle cx="76" cy="72" r="14" fill="#1f74c4"/><path d="M76 64v8h6" stroke="#fff" stroke-width="3" fill="none"/></svg>
      <span>Schedule Online Pickup</span>
    </div>
    <div class="step" style="left:338px">
      <svg width="116" height="116" viewBox="0 0 116 116"><circle cx="58" cy="58" r="55" fill="#fff" stroke="#ccc" stroke-width="3"/><circle cx="58" cy="38" r="10" fill="#f05a28"/><rect x="44" y="52" width="28" height="18" rx="4" fill="#f05a28"/><rect x="34" y="66" width="48" height="20" rx="3" fill="none" stroke="#1f74c4" stroke-width="4"/></svg>
      <span>We Will Pickup</span>
    </div>
    <div class="step" style="left:597px">
      <svg width="116" height="116" viewBox="0 0 116 116"><circle cx="58" cy="58" r="55" fill="#fff" stroke="#ccc" stroke-width="3"/><rect x="36" y="30" width="44" height="56" rx="5" fill="#f05a28"/><circle cx="58" cy="62" r="15" fill="#fff"/><circle cx="58" cy="62" r="9" fill="#1f74c4"/></svg>
      <span>We Wash &amp; Fold</span>
    </div>
    <div class="step" style="left:858px">
      <svg width="116" height="116" viewBox="0 0 116 116"><circle cx="58" cy="58" r="55" fill="#fff" stroke="#ccc" stroke-width="3"/><rect x="26" y="46" width="40" height="28" fill="#f05a28"/><path d="M66 54h14l10 10v10H66z" fill="#f05a28"/><circle cx="38" cy="78" r="6" fill="#1f74c4"/><circle cx="78" cy="78" r="6" fill="#1f74c4"/><circle cx="52" cy="36" r="12" fill="#fff" stroke="#1f74c4" stroke-width="3"/><path d="M46 36l4 4 8-8" stroke="#1f74c4" stroke-width="3" fill="none"/></svg>
      <span>Here We Deliver</span>
    </div>
  </div>
  <div class="perks">
    <div class="perk"><i></i>Only $1.10 only per pound</div>
    <div class="perk"><i></i>Free Pickup and Delivery</div>
    <div class="perk"><i></i>Same Day Pickup</div>
    <div class="perk"><i></i>Next Day Delivery</div>
    <div class="perk"><i></i>Schedule Online 24/7</div>
    <div class="perk"><i></i>Service in all NYC</div>
  </div>
</section>

<section class="testimonial center">
  <div class="testimonial-bg" role="img" aria-label="Dimmed laundromat interior with washing machines"></div>
  <h2>WHAT THEY SAID</h2>
  <blockquote>“The detergent that you guys use smells so good!, I’ve gotten complements on the smell!”</blockquote>
  <cite>Ashley - Manhattan</cite>
  <div class="dots"><i></i><i></i><i></i></div>
</section>

<section class="services">
  <div class="card card-a">
    <div class="photo" role="img" aria-label="Stack of folded white towels"></div>
    <div class="card-caption"><strong>Customized Commercial Laundry Service</strong><small>Click here for more info »</small></div>
  </div>
  <div class="card card-b">
    <div class="photo" role="img" aria-label="Delivery van loaded with blue laundry bags"></div>
    <div class="card-caption"><strong>Laundry Pickup and Delivery 7 Days a Week</strong><small>Click here for more info »</small></div>
  </div>
</section>

<section class="clients center">
  <h2 class="section-title">Our Clients</h2>
  <p class="subtitle">Check out some of our Customers</p>
  <div class="client-row">
    <div class="client"><i></i>Veltra</div>
    <div class="client">Corvane</div>
    <div class="client">Halden</div>
    <div class="client">Orsino</div>
    <div class="client">Brimwell</div>
  </div>
</section>

<section class="callband">
  <p>If you have any question about us call us : <span>(212) 555-0148</span></p>
</section>

<footer class="site-footer">
  <div class="col col-links">
    <h4>LINKS</h4>
    <ul><li>Home</li><li>Clean my Clothes</li><li>Pricing</li><li>Blog</li><li>Service Area</li><li>Commercial/Wholesale</li><li>Sign in</li></ul>
  </div>
  <div class="col col-contact">
    <h4>CONTACT</h4>
    <p class="email">orders@brisklinenhub.com</p>
    <p>(212) 555-0148</p>
    <ul class="social"><li><i></i>Chirp</li><li><i></i>Facet</li><li><i></i>Snapgram</li><li><i></i>Plusly</li></ul>
  </div>
  <div class="col col-address">
    <h4>ADDRESS</h4>
    <p>48 Harbor Lane, NY,<br>NY, 10006, USA<br>00000</p>
  </div>
  <p class="legal">Brisk Linen Hub LLC © 2015 | Terms of Service | Privacy Policy</p>
  <div class="contact-tab">Contact Us</div>
</footer>

</body>
</html>
```